・Webサイト作成サービス『ミモザ・サイトキット』内で、利用者が選択できるデザインテーマの新規作成依頼です。
・既存デザインとは異なる雰囲気のデザイン作成をお願いします。
・トップページのデザイン採用後、同テイストで一部下層ページのデザイン作成も依頼予定です

既存デザイン(サンプルサイトです)
https://sample.velorn.jp/

■サービス概要
・保険代理店向けのサブスクサービスです
・ノーコードでWebサイトを作成できます
・専用の管理画面から情報の追加や更新を行います
・Webサイトのデザインテーマも管理画面から選択します

サービスサイト
https://lp.velorn.jp/
・優しさを感じる「アットホーム」なデザインを希望します
・要素の角に丸みを持ったデザインとしてください
・色はブルー系で同系色にまとめてください
※ サービス移植後は基本色を変更し、12色での展開を予定しているため
・写真やバナー等の画像は既存サイトより保存して組み込んでください
※ 画像等はサービス共通のため、デザインいただく必要ありません
・表示内容は既存サイトを参考としてください
・CSSを変更するだけで対応可能な程度であれば多少のレイアウト変更はOKです
※ HTMLはそのままで、CSSを切り替えるだけでデザインを変える仕組みのため

■納品形式
Adobe XD での納品をお願いします。
https://sample.velorn.jp/
1ページ
青系
■納品形式
Adobe XD での納品をお願いします。
ページに表示するコンテンツの構成は変更できませんが、CSSで変更できる範囲で既存デザインとの違いを出したり、見た目の工夫をお願いします。

例えば...
・CSSの疑似要素を活用して見出しにあしらいを付ける
・背景へパターンを適用する
・お問い合わせボタンを絶対値で指定する
・既存のあしらい要素を非表示にする

さらに詳しく添付の画像に記載しておりますので、ご参照ください。
ご質問等あればお気軽にお願いします。

当該ランサーさんの初期の提案が、こちらの望んでいた雰囲気に一番近く、細かい部分にも丁寧な仕事ぶりが見られたことから、お声がけさせていただきました。
手直しの際もこちらの意図をしっかりと汲み取っていただき、少ない回数で望んだデザインへと至ることができました。

たくさんのご提案ありがとうございました。
また機会がございましたら、よろしくお願いいたします。

```html
<!DOCTYPE html>
<html lang="ja">
<head>
<meta charset="utf-8">
<title>サンプル保険サービス</title>
<link href="https://fonts.googleapis.com/css2?family=Noto+Sans+JP:wght@400;500;700&family=Noto+Serif+JP:wght@500;700&display=swap" rel="stylesheet">
<style>
:root{
  --blue:#1e88e5;
  --blue-dark:#1565c0;
  --blue-light:#e3f2fd;
  --blue-pale:#f2f8fe;
  --wood1:#d9d2c8;
  --wood2:#c9c0b4;
  --text:#333;
  --sub:#777;
  --white:#fff;
  --grey:#bdbdbd;
}
*{box-sizing:border-box;margin:0;padding:0}
html,body{width:1200px;height:3744px;overflow:hidden}
body{font-family:"Noto Sans JP",sans-serif;color:var(--text);background:var(--white);position:relative;font-size:15px}
.wood{background:linear-gradient(180deg,var(--wood1),var(--wood2) 50%,var(--wood1))}
section,header,footer{position:absolute;left:0;width:1200px}

/* header */
.site-header{top:0;height:100px;background:var(--white)}
.brand{position:absolute;left:40px;top:24px;display:flex;align-items:center;gap:10px;font-size:22px;font-weight:700;color:var(--blue-dark)}
.brand-dot{width:26px;height:26px;border-radius:50%;background:var(--blue)}
.head-tel{position:absolute;right:180px;top:10px;font-size:13px;color:var(--blue-dark)}
.head-tel b{font-size:18px}
.head-cta{position:absolute;right:20px;top:6px;width:150px;height:30px;border-radius:15px;background:var(--blue);color:#fff;font-size:12px;text-align:center;line-height:30px}
.gnav{position:absolute;right:30px;top:54px;display:flex;gap:10px}
.gnav a{display:block;width:120px;height:34px;line-height:34px;text-align:center;font-size:13px;border-radius:17px;color:var(--blue-dark);background:var(--blue-pale);text-decoration:none}
.gnav a.current{background:var(--blue);color:#fff}

/* hero */
.hero{top:100px;height:470px}
.hero-photo{position:absolute;left:40px;top:20px;width:1120px;height:420px;border-radius:28px;background:linear-gradient(135deg,#f4f6f8,#dfe8ef 50%,#c9d8e4)}
.hero-copy{position:absolute;left:110px;top:350px;font-family:"Noto Serif JP",serif;font-size:38px;font-weight:700;line-height:1.55;color:var(--blue-dark)}
.hero-copy span{display:inline-block;background:rgba(255,255,255,.85);padding:0 12px;border-radius:8px}
.hero-copy .em{background:var(--blue);color:#fff}

/* news */
.news{top:590px;height:280px}
.news-list{position:absolute;left:40px;top:20px;width:1120px;list-style:none}
.news-item{display:flex;align-items:center;height:60px;margin-bottom:16px;background:var(--white);border-radius:30px;box-shadow:0 3px 10px rgba(30,136,229,.18);padding:0 40px}
.news-item::before{content:"";width:12px;height:12px;border-radius:50%;background:var(--blue);margin-right:20px}
.news-item time{font-size:13px;color:var(--sub);margin-right:20px}
.news-title{flex:1;font-size:14px}
.news-tag{width:110px;height:26px;border-radius:13px;background:var(--blue);color:#fff;font-size:12px;text-align:center;line-height:26px;margin-right:260px}
.news-more{position:absolute;right:60px;top:230px;width:150px;height:34px;border:2px solid var(--blue);border-radius:17px;text-align:center;line-height:30px;color:var(--blue);font-size:13px}

/* feature cards */
.features{top:900px;height:400px}
.feature{position:absolute;top:50px;width:340px;height:300px}
.feature-photo{height:190px;border-radius:22px}
.feature-box{position:absolute;left:20px;top:110px;width:300px;height:150px;background:#fff;border-radius:20px;box-shadow:0 4px 14px rgba(0,0,0,.12);padding:50px 20px 0;font-size:12px;line-height:1.7;color:var(--sub);text-align:center}
.feature-title{position:absolute;left:50%;top:-18px;transform:translateX(-50%);width:210px;height:40px;line-height:40px;border-radius:20px;background:var(--blue);color:#fff;font-size:15px;font-weight:700}
.f1{left:60px}.f1 .feature-photo{background:linear-gradient(135deg,#b8d98b,#5d9c46)}
.f2{left:430px;top:20px}.f2 .feature-photo{background:linear-gradient(135deg,#fdf5d8,#e9d27a)}
.f3{left:800px}.f3 .feature-photo{background:linear-gradient(135deg,#dce6ef,#8aa0b6)}

/* online services */
.online{top:1340px;height:680px}
.ribbon{position:absolute;left:330px;top:20px;width:540px;height:74px;background:var(--blue);color:#fff;text-align:center;padding-top:8px;border-radius:6px;box-shadow:0 4px 0 var(--blue-dark)}
.ribbon h2{font-size:26px;font-weight:700;letter-spacing:.1em}
.ribbon small{font-size:12px;letter-spacing:.15em}
.service-figure{position:absolute;left:230px;top:130px;width:740px;height:500px;border-radius:28px;background:radial-gradient(circle at 50% 50%,#ffffff 30%,#e3f2fd 60%,#cfe6fb)}

/* links */
.links{top:2060px;height:300px}
.links-head{position:absolute;left:470px;top:20px;width:260px;height:50px;line-height:50px;text-align:center;background:var(--blue);color:#fff;font-weight:700;font-size:18px;border-radius:8px;border:3px solid #fff}
.link-banner{position:absolute;top:160px;width:240px;height:90px;background:#fff;border-radius:18px;box-shadow:0 4px 12px rgba(0,0,0,.15);display:flex;align-items:center;justify-content:center;gap:10px;font-weight:700;color:var(--blue-dark);font-size:18px}
.link-banner i{width:28px;height:28px;background:var(--blue);border-radius:4px}
.link-banner.social{background:var(--blue-dark);color:#fff}
.link-banner.social i{background:#fff;border-radius:50%}

/* contact */
.contact{top:2440px;height:240px}
.contact-box{position:absolute;left:230px;top:0;width:740px;height:210px;background:var(--blue);border-radius:30px;border:6px solid var(--blue-light);display:flex;align-items:center;justify-content:space-around;color:#fff}
.contact-tel{font-size:40px;font-weight:700;line-height:1.2}
.contact-tel small{display:block;font-size:14px;font-weight:500}
.contact-btn{width:250px;height:66px;background:#fff;color:var(--blue);border-radius:33px;text-align:center;line-height:66px;font-weight:700;font-size:18px}

/* access */
.access{top:2740px;height:600px}
.company{position:absolute;left:40px;top:30px;width:540px;height:260px;background:#fff;border-radius:22px;padding:30px 40px;font-size:13px;line-height:1.9}
.company h3{font-size:14px;margin-bottom:6px}
.map{position:absolute;left:620px;top:30px;width:540px;height:260px;border-radius:22px;background:linear-gradient(135deg,#e8edf0,#cfe0ea 60%,#b5cfdf)}
.notice{position:absolute;left:60px;top:320px;width:1080px;height:240px;background:#fff;border-radius:22px;padding:30px 40px;font-size:12px;line-height:2;color:#555}

/* footer */
.site-footer{top:3360px;height:384px;background:var(--blue);color:#fff}
.f-banners{position:absolute;left:110px;top:40px;display:flex;gap:70px}
.f-banners span{width:190px;height:60px;background:var(--grey);border-radius:14px;text-align:center;line-height:60px;color:#fff;font-weight:700}
.f-nav{position:absolute;left:110px;top:150px;display:grid;grid-template-columns:repeat(6,170px);row-gap:14px;font-size:14px}
.f-meta{position:absolute;left:0;width:1200px;top:300px;text-align:center;font-size:12px}
.copy{position:absolute;left:0;width:1200px;top:340px;text-align:center;font-size:13px}
</style>
</head>
<body>

<header class="site-header">
  <div class="brand"><span class="brand-dot"></span>サンプル保険サービス</div>
  <div class="head-tel">平日9:00-17:00（土日祝・休み） <b>☎123-456-7890</b></div>
  <div class="head-cta">お問い合わせはこちら</div>
  <nav class="gnav">
    <a class="current">ホーム</a><a>当社について</a><a>サービスのご案内</a><a>スタッフ紹介</a><a>お知らせ</a>
  </nav>
</header>

<section class="hero wood">
  <div class="hero-photo" role="img" aria-label="笑顔の家族の写真"></div>
  <p class="hero-copy"><span>お客さま一人ひとりに合った</span><br><span class="em">保険</span><span>を提案します</span></p>
</section>

<section class="news">
  <ul class="news-list">
    <li class="news-item"><time>2022.04.01</time><span class="news-title">新型コロナウイルスの当社対応について</span><span class="news-tag">お知らせ</span></li>
    <li class="news-item"><time>2022.03.15</time><span class="news-title">新型コロナウイルスの当社対応について</span><span class="news-tag">お知らせ</span></li>
    <li class="news-item"><time>2022.03.01</time><span class="news-title">新型コロナウイルスの当社対応について</span><span class="news-tag">お知らせ</span></li>
  </ul>
  <div class="news-more">一覧 →</div>
</section>

<section class="features wood">
  <article class="feature f1">
    <div class="feature-photo" role="img" aria-label="木漏れ日と緑の葉の写真"></div>
    <div class="feature-box"><h3 class="feature-title">当社について</h3>会社概要、アクセスなど<br>当社についての情報を<br>ご紹介しています。</div>
  </article>
  <article class="feature f2">
    <div class="feature-photo" role="img" aria-label="保険の書類とペンの写真"></div>
    <div class="feature-box"><h3 class="feature-title">サービスのご案内</h3>各保険の商品内容をはじめ<br>お申込み、お手続き方法を<br>ご案内しています。</div>
  </article>
  <article class="feature f3">
    <div class="feature-photo" role="img" aria-label="スーツ姿のスタッフの写真"></div>
    <div class="feature-box"><h3 class="feature-title">スタッフ紹介</h3>各担当のプロフィールや<br>ご相談できる内容を<br>ご紹介しています。</div>
  </article>
</section>

<section class="online">
  <div class="ribbon"><h2>オンラインサービス</h2><small>online service</small></div>
  <div class="service-figure" role="img" aria-label="青い輪の周りに各保険会社のオンラインサービスのバナーが並ぶ図"></div>
</section>

<section class="links wood">
  <h2 class="links-head">関連リンク</h2>
  <a class="link-banner" style="left:90px"><i></i>サンプル保険</a>
  <a class="link-banner" style="left:360px"><i></i>SAMPLE生命</a>
  <a class="link-banner" style="left:630px"><i></i>サンプル生命</a>
  <a class="link-banner social" style="left:900px"><i></i>フォトシェア</a>
</section>

<section class="contact">
  <div class="contact-box">
    <p class="contact-tel">☎123-456-7890<small>平日9:00-17:00（土日祝・休み）</small></p>
    <a class="contact-btn">お問い合わせはこちら</a>
  </div>
</section>

<section class="access wood">
  <div class="company">
    <h3>● 会社概要</h3>
    サンプル保険サービス株式会社<br>
    〒000-0000<br>
    東京都千代田区サンプル町1-2-3 サンプルビル5F<br><br>
    TEL：123-456-7890<br>
    FAX：123-456-7899
  </div>
  <div class="map" role="img" aria-label="周辺の地図"></div>
  <div class="notice">
    ・この記載内容はサンプルです。保険商品の詳細については各保険会社の案内をご確認ください。<br>
    ・当社は複数の保険会社の代理店として保険契約の締結の媒介を行っております。<br>
    ・ご契約の際は重要事項説明書を必ずお読みいただき、内容を十分にご確認ください。<br>
    ・お客さまの個人情報は保険のご案内およびお手続きの目的にのみ利用いたします。<br>
    ・ご不明な点がございましたら、お気軽に当社窓口までお問い合わせください。
  </div>
</section>

<footer class="site-footer">
  <div class="f-banners"><span>バナー</span><span>バナー</span><span>バナー</span><span>バナー</span></div>
  <nav class="f-nav">
    <a>ホーム</a><a>当社について</a><a>サービスのご案内</a><a>スタッフの紹介</a><a>お知らせ</a><a></a>
    <a>勧誘方針</a><a>情報取扱方針</a><a>個人情報保護方針</a><a>保険業法上の方針</a><a>苦情対応方針</a><a>サイトマップ</a>
  </nav>
  <p class="f-meta">▲ ページトップへ</p>
  <p class="copy">©2021-2022 サンプル保険サービス株式会社</p>
</footer>

</body>
</html>
```